Hacienda Las Bruneras Website

I need a template design for Hacienda Las Bruneras which is a Residential and Commercial development project to be located in Panama.

The look of the website has to be "country" since it is a Hacienda. It has to take in the feel of being out with nature.

The Logo of the project is contained in the attached files as well as pictures of the Project´s conceptual design and several air pictures of the land where the project will be built.

Industry/Entity Type

Residential

Requirements
Must have
• The website has to be very simple, very visual, a lot of images. The Main Menu has to be:
1. Home
2. About us
3. The project
4. Location
5. Contact us

```html
<!DOCTYPE html>
<html lang="en">
<head>
<meta charset="utf-8">
<title>Hacienda Las Bruneras</title>
<link href="https://fonts.googleapis.com/css2?family=Arimo:wght@400;700&family=Kaushan+Script&family=Oswald:wght@600&display=swap" rel="stylesheet">
<style>
:root{
  --cream:#f8e2bb;
  --cream-frame:#f3d9a5;
  --panel:#f5e0b9;
  --brown:#8a5c1b;
  --brown-dark:#6e4812;
  --heading:#8a5c1b;
  --ink:#222;
  --nav:#3a2a10;
  --white:#fff;
  --caption:rgba(38,30,22,.88);
  --rule:#c9a667;
  --red:#e01010;
  --grey:#555;
}
*{margin:0;padding:0;box-sizing:border-box}
html,body{width:970px;height:1200px;overflow:hidden;background:var(--white)}
body{position:relative;font-family:"Arimo",Arial,sans-serif;color:var(--ink)}
.abs{position:absolute}
.header{left:0;top:0;width:970px;height:96px;background:var(--cream)}
.brand{left:106px;top:28px;display:flex;align-items:center;gap:10px;font-size:24px;font-weight:700;color:var(--brown)}
.brand-mark{width:26px;height:26px;border-radius:50%;background:var(--brown)}
.nav a{position:absolute;top:56px;font-size:13px;color:var(--nav);text-decoration:none}
.hero-band{left:0;top:96px;width:970px;height:290px;background:var(--brown)}
.frame{border:4px solid var(--cream-frame)}
.photo-sky{background:linear-gradient(#3d7fcf 0%,#9ec4ea 40%,#4d7a3a 70%,#2f5a2a 100%)}
.photo-aerial{background:linear-gradient(#a7b7c2 0%,#6f8f55 30%,#4f7a3a 70%,#6c7a4a 100%)}
.photo-render{background:linear-gradient(#1f3a20,#50705a 50%,#8a8f90)}
.photo-street{background:linear-gradient(#4a6aa0 0%,#d8b58a 30%,#556b48 55%,#8e9296 100%)}
.caption{left:276px;top:337px;width:320px;height:42px;background:var(--caption);color:var(--white);font-size:16px;display:flex;align-items:center;justify-content:center}
.story{position:absolute;left:606px;width:281px;border-bottom:1px solid var(--rule);height:62px}
.story-thumb{position:absolute;left:0;top:0;width:91px;height:48px;border:3px solid var(--cream-frame)}
.story-title{position:absolute;left:101px;top:2px;font-size:10px;font-weight:700;color:var(--white)}
.story-text{position:absolute;left:101px;top:16px;width:180px;font-size:9px;line-height:11px;color:#f6e6c8}
.tile{position:absolute;top:398px;height:110px;border:4px solid var(--cream-frame)}
.plus{position:absolute;left:50%;top:50%;width:26px;height:26px;margin:-13px 0 0 -13px;border-radius:50%;background:rgba(138,92,27,.9)}
.h{position:absolute;font-size:15px;color:var(--heading)}
.copy{position:absolute;width:210px;font-size:10.5px;line-height:17px;color:var(--ink)}
.copy p+p{margin-top:12px}
.divider{position:absolute;top:540px;width:1px;height:168px;background:var(--rule)}
.play{position:absolute;left:50%;top:50%;width:28px;height:28px;margin:-14px 0 0 -14px;border-radius:50%;background:rgba(138,92,27,.9)}
.first-look{left:529px;top:580px;font-family:"Kaushan Script",cursive;font-size:14px;color:var(--ink)}
.watch{left:529px;top:606px;font-size:19px;font-weight:700;color:var(--red)}
.choice{left:529px;top:639px;font-family:"Oswald",sans-serif;font-size:14px;color:var(--grey)}
.carousel{left:104px;top:1016px;width:804px;height:128px;background:var(--panel);border-radius:10px}
.slide{position:absolute;top:1028px;height:102px;border:1px solid #444}
.footer{left:0;top:1162px;width:970px;height:38px;background:var(--brown);color:var(--white);font-size:10px}
.footer .links{position:absolute;left:107px;top:18px}
.footer .rights{position:absolute;right:66px;top:19px}
</style>
</head>
<body>
<header class="abs header">
  <div class="abs brand"><span class="brand-mark"></span>Hacienda Las Bruneras</div>
  <nav class="nav">
    <a style="left:539px">Home</a>
    <a style="left:604px">About us</a>
    <a style="left:676px">The project</a>
    <a style="left:760px">Location</a>
    <a style="left:832px">Contact us</a>
  </nav>
</header>

<section class="abs hero-band"></section>
<div class="abs frame photo-sky" style="left:108px;top:119px;width:479px;height:242px" role="img" aria-label="Rendering of the brick entrance gateway with trees and blue sky"></div>
<div class="abs caption">Entrada Las Bruneras</div>

<div class="story" style="top:120px">
  <div class="story-thumb photo-sky" role="img" aria-label="Entrance gateway thumbnail"></div>
  <div class="story-title">Entrada Las Bruneras</div>
  <div class="story-text">Getting Started contains a list of tasks you might want to perform when you set up your computer.</div>
</div>
<div class="story" style="top:212px">
  <div class="story-thumb photo-sky" role="img" aria-label="Entrance gateway thumbnail"></div>
  <div class="story-title">Entrada Las Bruneras</div>
  <div class="story-text">Getting Started contains a list of tasks you might want to perform when you set up your computer.</div>
</div>
<div class="story" style="top:301px">
  <div class="story-thumb photo-sky" role="img" aria-label="Entrance gateway thumbnail"></div>
  <div class="story-title">Entrada Las Bruneras</div>
  <div class="story-text">Getting Started contains a list of tasks you might want to perform when you set up your computer.</div>
</div>

<div class="tile photo-aerial" style="left:104px;width:188px" role="img" aria-label="Aerial view of green hills and road"><span class="plus"><svg width="26" height="26"><path d="M13 7v12M7 13h12" stroke="#fff" stroke-width="2"/></svg></span></div>
<div class="tile photo-aerial" style="left:311px;width:186px" role="img" aria-label="Aerial view of highway through land"><span class="plus"><svg width="26" height="26"><path d="M13 7v12M7 13h12" stroke="#fff" stroke-width="2"/></svg></span></div>
<div class="tile photo-aerial" style="left:517px;width:186px" role="img" aria-label="Aerial view of road and village"><span class="plus"><svg width="26" height="26"><path d="M13 7v12M7 13h12" stroke="#fff" stroke-width="2"/></svg></span></div>
<div class="tile photo-aerial" style="left:724px;width:186px" role="img" aria-label="Aerial view of cleared land and trees"><span class="plus"><svg width="26" height="26"><path d="M13 7v12M7 13h12" stroke="#fff" stroke-width="2"/></svg></span></div>

<h2 class="h" style="left:104px;top:550px">Heading</h2>
<div class="copy" style="left:107px;top:580px">
  <p>The look of the website has to be "country" since it is a Hacienda. It has to take in the feel of being out with nature.</p>
  <p>The look of the website has to be "country" since it is a Hacienda. It has to take in the feel of being out with nature.</p>
</div>
<div class="divider" style="left:367px"></div>
<h2 class="h" style="left:381px;top:550px">Heading</h2>
<div class="abs frame photo-aerial" style="left:380px;top:572px;width:137px;height:104px" role="img" aria-label="Aerial video preview of the land"><span class="play"><svg width="28" height="28"><path d="M11 8l9 6-9 6z" fill="#fff"/></svg></span></div>
<div class="abs first-look">First Look</div>
<div class="abs watch">WATCH !</div>
<div class="abs choice">Select Your Choice</div>
<div class="divider" style="left:648px"></div>
<h2 class="h" style="left:658px;top:550px">Heading</h2>
<div class="copy" style="left:660px;top:580px">
  <p>The look of the website has to be "country" since it is a Hacienda. It has to take in the feel of being out with nature.</p>
  <p>The look of the website has to be "country" since it is a Hacienda. It has to take in the feel of being out with nature.</p>
</div>

<h2 class="h" style="left:104px;top:720px">Headings</h2>
<div class="abs frame photo-render" style="left:106px;top:748px;width:392px;height:202px" role="img" aria-label="Rendering of the roundabout with garden and cypress trees"></div>
<div class="abs frame photo-street" style="left:518px;top:748px;width:393px;height:202px" role="img" aria-label="Rendering of the tree-lined main street at sunset"></div>

<h2 class="h" style="left:104px;top:983px">Heading</h2>
<div class="abs carousel"></div>
<svg class="abs" style="left:118px;top:1062px" width="24" height="40"><path d="M20 2L6 20l14 18" fill="none" stroke="#e3c48e" stroke-width="6"/></svg>
<svg class="abs" style="left:880px;top:1062px" width="24" height="40"><path d="M4 2l14 18L4 38" fill="none" stroke="#e3c48e" stroke-width="6"/></svg>
<div class="slide photo-aerial" style="left:156px;width:155px" role="img" aria-label="Aerial photo of forested land"></div>
<div class="slide photo-aerial" style="left:328px;width:166px" role="img" aria-label="Aerial photo of land with dirt paths"></div>
<div class="slide photo-aerial" style="left:510px;width:167px" role="img" aria-label="Aerial photo of green valley"></div>
<div class="slide photo-aerial" style="left:690px;width:174px" role="img" aria-label="Aerial photo of hills and horizon"></div>

<footer class="abs footer">
  <div class="links">Home | &nbsp;Privacy Policy | Disclaimer</div>
  <div class="rights">All right reserved 2013-14</div>
</footer>
</body>
</html>
```